Business Card for Freelance Copywriting & Web Design Business

Hi! I have a logo but want a new business card. Here's a better idea of what I'm thinking:
-Brand new double-sided business card, rounded cards, embossed logo, nice quality paper
-Include phone (604-382-9145), email (hello@linnearowatt.org), and website (www.linnearowatt.org). No address, please, since I service clients worldwide.
-I'd like the fonts to match those on my website (www.linnearowatt.org). I had to purchase the one font (Born Ready), attached. I'm not sure which version was used on my site so I included all that I purchased. The secondary font is Helvetica
-I'd also like the tagline "Powerful Words. Impressive Results." included.
-My primary brand colour is the teal, colour #19ADC3
Linnea Rowatt | Linnea Rowatt Copywriting & Web Design <hello@linnearowatt.org>
-I'd also like the following services listed on the new cards:
SEO Website Content
SEO Blog Content
SEO Website Design
Contact Information for Business Card
as stated in brief
Font styles to use
Other font styles liked:
- See brief
Look and feel
Each slider illustrates characteristics of the customer's brand and the style your logo design should communicate.

```html
<!DOCTYPE html>
<html lang="en">
<head>
<meta charset="utf-8">
<title>Linnea Rowatt – Business Card</title>
<link rel="stylesheet" href="https://fonts.googleapis.com/css2?family=Arimo:wght@400;700&display=swap">
<style>
  :root {
    --backdrop: #d4d9d9;
    --card: #f0f0f0;
    --teal: #74b3bf;
    --teal-light: #86c2cd;
    --ink: #161616;
  }
  * { margin: 0; padding: 0; box-sizing: border-box; }
  html, body { width: 1200px; height: 960px; overflow: hidden; }
  body {
    background: var(--backdrop);
    font-family: "Arimo", Helvetica, Arial, sans-serif;
    color: var(--ink);
    position: relative;
  }
  .card {
    position: absolute;
    left: 252px;
    width: 699px;
    height: 400px;
    background: var(--card);
    border-radius: 26px;
    border-left: 4px solid var(--teal);
    border-bottom: 4px solid var(--teal);
    overflow: hidden;
  }
  .card--front { top: 60px; }
  .card--back { top: 500px; }

  .wordmark {
    position: absolute;
    font-weight: 400;
    color: var(--ink);
    white-space: nowrap;
    letter-spacing: 0.5px;
  }
  .card--front .wordmark {
    left: 0; right: 0; top: 150px;
    text-align: center;
    font-size: 50px;
  }
  .card--back .wordmark {
    left: 26px; top: 85px;
    font-size: 40px;
  }

  .services {
    position: absolute;
    left: 0; right: 0; top: 322px;
    text-align: center;
  }
  .services__title {
    color: var(--teal-light);
    font-size: 20px;
    font-weight: 400;
    letter-spacing: 0.5px;
  }
  .services__list {
    list-style: none;
    display: flex;
    justify-content: center;
    gap: 12px;
    margin-top: 6px;
    font-size: 16.5px;
  }
  .services__list li::before {
    content: "";
    display: inline-block;
    width: 8px; height: 8px;
    border-radius: 50%;
    background: var(--teal-light);
    margin-right: 9px;
    vertical-align: 2px;
  }

  .identity {
    position: absolute;
    right: 36px; top: 36px;
    text-align: right;
  }
  .identity__name {
    color: var(--teal-light);
    font-size: 34px;
    font-weight: 700;
    line-height: 1;
    letter-spacing: 0.3px;
  }
  .identity__role {
    font-size: 16px;
    margin-top: 4px;
  }
  .identity-bar {
    position: absolute;
    right: 0; top: 31px;
    width: 18px; height: 61px;
    background: var(--teal);
  }

  .tagline {
    position: absolute;
    left: 18px; top: 236px;
    color: var(--teal-light);
    font-size: 16px;
    line-height: 22px;
  }

  .contact {
    position: absolute;
    left: 18px; top: 303px;
    list-style: none;
    font-size: 16px;
  }
  .contact li {
    display: flex;
    align-items: center;
    height: 23.5px;
  }
  .contact svg {
    width: 17px; height: 17px;
    margin-right: 11px;
    fill: none;
    stroke: var(--teal);
    stroke-width: 1.8;
  }
</style>
</head>
<body>

  <section class="card card--front">
    <div class="wordmark">Linnea Rowatt</div>
    <div class="services">
      <h2 class="services__title">SERVICES</h2>
      <ul class="services__list">
        <li>SEO Website Content</li>
        <li>SEO Blog Content</li>
        <li>SEO Website Design</li>
      </ul>
    </div>
  </section>

  <section class="card card--back">
    <div class="wordmark">Linnea Rowatt</div>

    <div class="identity">
      <div class="identity__name">Linnea Rowatt</div>
      <div class="identity__role">Copywriting &amp; Web Design</div>
    </div>
    <div class="identity-bar"></div>

    <p class="tagline">Powerful Words.<br>Impressive Results.</p>

    <ul class="contact">
      <li>
        <svg viewBox="0 0 24 24" aria-hidden="true"><path d="M5 3h4l2 5-2.5 1.5a11 11 0 0 0 6 6L16 13l5 2v4a2 2 0 0 1-2 2A16 16 0 0 1 3 5a2 2 0 0 1 2-2z"/></svg>
        (604-382-9145)
      </li>
      <li>
        <svg viewBox="0 0 24 24" aria-hidden="true"><circle cx="12" cy="12" r="9.5"/><path d="M2.5 12h19M12 2.5c3 3 3 16 0 19M12 2.5c-3 3-3 16 0 19"/></svg>
        www.linnearowatt.org
      </li>
      <li>
        <svg viewBox="0 0 24 24" aria-hidden="true"><rect x="2.5" y="5" width="19" height="14" rx="1"/><path d="M2.5 6l9.5 7 9.5-7"/></svg>
        hello@linnearowatt.org
      </li>
    </ul>
  </section>

</body>
</html>
```